Flyer Design für Kosmetikerin und Visagistin gesucht
Zielgruppe
Ich bin ein Einmannbetrieb und biete Kosmetik für Frauen, Männer und Jugendliche, Visagistik, Nageldesign und Wimpernverlängerun an - eine bestimmte Zielgruppe gibt es eigentlich nicht - es sollen alle angesprochen werden.
Aufgabenstellung
Ich hätte gerne einen Flyer, welcher beidseitig bedruckt wird und welchen ich dann per Postwurfsendung an die Haushalte in meiner Umgebung verteilen kann, da ich gerade mein Kosmetikstudio eröffnet habe. Auf der Vorderseite hätte ich gerne meinen Namen, Dipl. Kosmetikerin, Dipl. Make-up-Artist, Dipl. Nageldesignerin, meine Adresse (eventuell kleine Karte) und meine Telefonnummer mit dem Hinweis 'Termine nach telefonischer Vereinbarung' Und meine Mailadresse.
Weiters hätte ich gerne 'Neueröffnung', 'tolle Eröffnungsangbote bis Jahresende', 'kleines Willkommensgeschenk solange der Vorrat reicht' und den Satz 'der erste Eindruck hat keine zweite Chance' darauf. Ansonsten gilt bei der Vorderseite freie Gestaltung!
Auf der Rückseite hätte ich gerne meine Preisliste - ich lade sie mal als PDF-Datei hoch...
Ich lade auch mein Logo, meine Preisliste und ein paar Bilder hoch, die Bilder dürfen verwendet werden, denn ich habe dafür auch bezahlt - ist aber keine Pflicht - bin für jede andere Idee offen! Bevorzugten Farben sind Rosa und Pink, es darf auch versielt sein! Das Format, ob quer, hochgestellt, gefaltet usw. ist mir eigentlich egal - die Preisliste soll nur gut leserlich sein - kann auch von der Anordnung her verändert werden.

```html
<!DOCTYPE html>
<html lang="de">
<head>
<meta charset="utf-8">
<title>Faltblatt Neueröffnung – Glanzzeit</title>
<link href="https://fonts.googleapis.com/css2?family=Oswald:wght@500;700&family=Roboto+Condensed:wght@400;700&family=Alegreya+Sans:wght@400;500&display=swap" rel="stylesheet">
<style>
:root{
  --magenta:#b0127f;
  --magenta-dark:#8e0c66;
  --rose:#e9a8cd;
  --blush:#f6e1ee;
  --ink:#2b2b2b;
  --paper:#ffffff;
  --board:#ffffff;
  --skin-a:#f1d6c8;
  --skin-b:#d9a991;
  --hair:#5a3b2c;
}
*{box-sizing:border-box;margin:0;padding:0}
html,body{width:1200px;height:848px;overflow:hidden;background:var(--board)}
body{position:relative;font-family:"Roboto Condensed",sans-serif;color:var(--ink)}
.label{position:absolute;font-family:"Alegreya Sans",sans-serif;font-weight:500;font-size:22px;color:#111}
.spec{position:absolute;left:58px;top:426px;font-family:"Alegreya Sans",sans-serif;font-size:20px;line-height:23px;color:#111}
.sheet{position:absolute;background:var(--paper);overflow:hidden;box-shadow:0 2px 6px rgba(0,0,0,.25)}
.photo{position:absolute}
.skin{background:linear-gradient(135deg,var(--skin-a),var(--skin-b))}
.portrait{background:linear-gradient(160deg,var(--hair) 0%,#7b5140 35%,var(--skin-b) 60%,var(--skin-a) 100%)}
.orchid{background:radial-gradient(circle at 60% 45%,#b54aa6 0%,#d98fcf 30%,#f5e5f1 65%,#fff 100%)}
.nails{background:linear-gradient(150deg,#f4e2da,#e1b9a6 55%,#c9a6d8)}
.mask{background:linear-gradient(140deg,#eeeeee,#d8c2b4 55%,#b69483)}
.bar{position:absolute;left:0;right:0;background:var(--magenta)}
.brand{font-family:"Roboto Condensed",sans-serif;font-weight:700;color:var(--magenta);display:flex;align-items:center;justify-content:center;gap:5px}
.brand .dot{width:10px;height:10px;border-radius:50%;background:var(--rose)}

/* front panel */
.front{left:58px;top:52px;width:157px;height:330px}
.front .quote{position:absolute;left:8px;top:8px;width:145px;font-family:"Oswald",sans-serif;font-weight:500;font-size:10.5px;line-height:12px;color:#fff}
.front .headline{position:absolute;left:0;right:0;top:155px;text-align:center;font-family:"Oswald",sans-serif;font-weight:700;font-size:19px;color:var(--magenta);-webkit-text-stroke:.4px #fff}
.front .badge{position:absolute;left:46px;top:183px;width:48px;height:48px;border-radius:50%;background:var(--magenta);color:#fff;font-size:5.6px;font-weight:700;line-height:6.4px;text-align:center;display:flex;align-items:center;justify-content:center;padding:4px}
.front .gift{position:absolute;left:98px;top:184px;width:58px;color:#fff;font-size:5.4px;line-height:6.2px;font-weight:700}
.front .gift small{display:block;font-size:3.4px;font-weight:400}
.front .brand{position:absolute;left:0;right:0;top:270px;font-size:20px}
.front .services{position:absolute;left:58px;right:10px;top:307px;background:var(--magenta);color:#fff;font-size:3.4px;text-align:center;padding:1px 0}

/* cover spread */
.cover{left:288px;top:53px;width:312px;height:329px}
.cover .top{position:absolute;left:0;top:0;width:312px;height:195px;background:var(--magenta);color:#fff}
.cover h1{position:absolute;left:7px;top:6px;font-family:"Oswald",sans-serif;font-weight:700;font-size:43px;letter-spacing:.5px;line-height:56px}
.cover .sub{position:absolute;left:8px;top:54px;font-family:"Oswald",sans-serif;font-weight:500;font-size:16.5px}
.cover .portrait-box{position:absolute;left:77px;top:79px;width:70px;height:86px;background:#fff;color:#555;font-size:4px;display:flex;align-items:center;justify-content:center}
.cover .greet{position:absolute;left:163px;top:79px;font-family:"Oswald",sans-serif;font-size:8.4px;line-height:10px}
.cover .sign{position:absolute;left:163px;top:102px;width:90px;height:64px;background:linear-gradient(120deg,rgba(255,255,255,.12),rgba(255,255,255,.25))}
.cover .motto{position:absolute;left:7px;top:172px;font-family:"Oswald",sans-serif;font-weight:500;font-size:13.5px}
.cover .photo{left:0;top:195px;width:312px;height:134px}
.cover .welcome{position:absolute;left:32px;top:203px;width:74px;height:74px;border-radius:50%;background:var(--magenta);color:#fff;font-family:"Oswald",sans-serif;font-size:8px;line-height:10px;text-align:center;display:flex;align-items:center;justify-content:center;transform:rotate(-10deg);box-shadow:0 1px 3px rgba(0,0,0,.3)}

/* inner spread */
.inner{left:288px;top:462px;width:577px;height:354px;border-top:5px solid var(--magenta);display:grid;grid-template-columns:repeat(4,1fr)}
.panel{position:relative;border-right:1px solid #eee;padding:8px 6px 0}
.panel:last-child{border-right:none}
.panel .photo{left:0;right:0;top:193px;bottom:0}
.title{font-weight:700;font-size:8px;color:var(--magenta);margin-bottom:6px}
.group{margin-bottom:5px}
.group h3{font-weight:400;font-size:4.4px;color:var(--magenta);margin-bottom:1px}
.row{display:flex;justify-content:space-between;font-size:4.2px;line-height:5.1px;gap:4px}
.row span:last-child{white-space:nowrap}
.note{font-weight:700;font-size:4.4px;margin-top:4px}

/* back panel */
.back{left:982px;top:460px;width:155px;height:330px}
.back .map{position:absolute;left:6px;top:8px;width:143px;height:105px;border:1px solid #ddd;background:#fafafa}
.back .brand{position:absolute;left:0;right:0;top:137px;font-size:15px}
.back .contact{position:absolute;left:0;right:0;top:177px;text-align:center;font-size:4.4px;line-height:6px}
.back .contact b{color:var(--magenta)}
.back .contact .name{font-weight:700;color:var(--ink)}
.back .appointment{position:absolute;left:33px;top:264px;width:90px;height:50px;background:var(--blush);border:1px solid #e3c3d6;font-size:4px;display:flex;align-items:flex-end;justify-content:center;padding-bottom:4px}
</style>
</head>
<body>

<div class="label" style="left:80px;top:14px">Vorderseite</div>
<div class="label" style="left:519px;top:422px">Innenseiten</div>
<div class="label" style="left:1011px;top:424px">Rückseite</div>

<div class="spec">Faltblatt | Einbruchfalz<br>DIN A5 lang<br>10,5 x 29,7 cm<br>&nbsp;4seitig<br>4/4-farbig</div>

<!-- Vorderseite -->
<section class="sheet front">
  <div class="photo portrait" style="left:0;top:0;width:157px;height:205px" role="img" aria-label="Porträtfoto einer geschminkten jungen Frau"></div>
  <p class="quote">„DER ERSTE EINDRUCK HAT KEINE ZWEITE CHANCE“</p>
  <p class="headline">NEUERÖFFNUNG</p>
  <div class="photo mask" style="left:0;top:205px;width:52px;height:52px" role="img" aria-label="Foto einer Gesichtsbehandlung"></div>
  <div class="photo nails" style="left:52px;top:205px;width:52px;height:52px" role="img" aria-label="Foto von Pinsel und Kristallen"></div>
  <div class="photo nails" style="left:104px;top:205px;width:53px;height:52px" role="img" aria-label="Foto gepflegter Hände mit Nageldesign"></div>
  <div class="badge">Tolle Eröffnungs-angebote bis Jahresende</div>
  <p class="gift">und ein kleines Willkommensgeschenk<small>(solange der Vorrat reicht)</small></p>
  <div class="brand"><span class="dot"></span>Glanzzeit</div>
  <div class="services">KOSMETIK | VISAGISTIK | NAGELDESIGN | WIMPERNVERLÄNGERUNG</div>
  <div class="bar" style="bottom:0;height:4px"></div>
</section>

<!-- Titel-Doppelseite -->
<section class="sheet cover">
  <div class="top">
    <h1>NEUERÖFFNUNG</h1>
    <p class="sub">Tolle Eröffnungsangebote bis Jahresende</p>
    <div class="portrait-box">FOTO</div>
    <p class="greet">Ich freue mich auf Sie!<br>Ihre Marlene Vogt</p>
    <div class="sign" role="img" aria-label="Handschriftliche Unterschrift"></div>
    <p class="motto">„DER ERSTE EINDRUCK HAT KEINE ZWEITE CHANCE“</p>
  </div>
  <div class="photo skin" role="img" aria-label="Foto einer entspannten Frau bei einer Kopfmassage"></div>
  <div class="welcome">Plus ein Willkommens-geschenk für Sie solange der Vorrat reicht!</div>
</section>

<!-- Innenseiten -->
<section class="sheet inner">
  <div class="panel">
    <p class="title">Preisliste 2013</p>
    <div class="group"><h3>Gesichtsbehandlung für Eilige</h3><div class="row"><span>Reinigung, Hautanalyse, Tonic, Peeling, Maske, Tagespflege</span><span>€ 25,00</span></div></div>
    <div class="group"><h3>Gesichtsbehandlung klassisch</h3><div class="row"><span>Reinigung, Hautanalyse, Peeling, Dampf, Ausreinigen, Tonic, Maske, Lippenpflege, Massage, Augen- u. Tagespflege</span><span>€ 38,00</span></div></div>
    <div class="group"><h3>Gesichtsbehandlung deluxe</h3><div class="row"><span>Reinigung, Hautanalyse, Peeling, Wimpern oder Augenbrauen färben, Dampf, Ausreinigen, Tonic, Ampulle, Maske, Lippenpflege, Massage</span><span>€ 52,00</span></div></div>
    <div class="group"><h3>Gesichtsbehandlung Anti-Age spezial</h3><div class="row"><span>Reinigung, Peeling, Dampf, Ausreinigen, Tonic, Ampulle oder Serum, Spezialmaske, Collagen-Vlies, Augenampulle, Massage, Tagespflege</span><span>€ 78,00</span></div></div>
    <div class="group"><h3>Mikrodermabrasionbehandlung</h3><div class="row"><span>Reinigung, Peeling, Mikrodermabrasion, Ampulle oder Serum, Maske, Tagespflege</span><span>€ 54,00</span></div><div class="row"><span>Kur 4x mit Wochenabstand</span><span>€ 205,00</span></div></div>
    <div class="photo mask" role="img" aria-label="Foto einer Gesichtsmaske, die mit dem Pinsel aufgetragen wird"></div>
  </div>
  <div class="panel">
    <div class="group"><h3>Fruchtsäurebehandlung</h3><div class="row"><span>Reinigung, Peeling, AHA-Fruchtsäuretonic, Ampulle, Massage mit Vit.C-Creme, Augen- u. Tagespflege</span><span>€ 58,00</span></div><div class="row"><span>Kur 4x mit Wochenabstand</span><span>€ 220,00</span></div></div>
    <div class="group"><h3>Mikrodermabrasion mit Fruchtsäure kombiniert</h3><div class="row"><span>Reinigung, Peeling, Mikrodermabrasion, AHA-Fruchtsäuretonic, Milchsäure-Vlies, Massage, Augen- und Tagespflege</span><span>€ 105,00</span></div><div class="row"><span>Kur 4x mit Wochenabstand</span><span>€ 410,00</span></div></div>
    <div class="group"><h3>Aknespezialbehandlung</h3><div class="row"><span>Reinigung, Peeling, Dampf, Ausreinigen, Tonic, Ampulle, Aknespezialmaske, Spezialpflege</span><span>€ 38,00</span></div></div>
    <div class="group"><h3>Pigmentfleckenspezialbehandlung</h3><div class="row"><span>Reinigung, Peeling, Dampf, Spezialserum, Spezialmaske gegen Pigmentflecken, Augenpflege</span><span>€ 48,00</span></div></div>
    <div class="group"><h3>Anticouperosespezialbehandlung</h3><div class="row"><span>Reinigung, Peeling, Dampf, Spezialserum, Spezialmaske, Augenpflege, Spezialpflege</span><span>€ 48,00</span></div><div class="row"><span>Gesicht-, Hals- und Dekolletémassage (ca. 20 min)</span><span>€ 18,00</span></div><div class="row"><span>Kosmetische Lymphdrainage (ca. 30 min)</span><span>€ 23,00</span></div></div>
    <div class="photo nails" role="img" aria-label="Foto gepflegter Hände mit French-Nageldesign"></div>
  </div>
  <div class="panel">
    <div class="group"><h3>Zusatzbehandlungen</h3>
      <div class="row"><span>Wimpern färben</span><span>€ 6,00</span></div>
      <div class="row"><span>Augenbrauen färben</span><span>€ 5,00</span></div>
      <div class="row"><span>Augenbrauen formen/zupfen</span><span>€ 4,00</span></div>
      <div class="row"><span>Augen-Intensivbehandlung</span><span>€ 18,00</span></div>
      <div class="row"><span>Wimperndauerwelle</span><span>€ 18,00</span></div>
      <div class="row"><span>Kinn oder Oberlippe harzen</span><span>€ 6,00</span></div>
      <div class="row"><span>Wirkstoffampulle</span><span>€ 8,00</span></div>
      <div class="row"><span>Hochfrequenz</span><span>€ 6,00</span></div></div>
    <div class="group"><h3>Cellulite-/Entschlackungswickel</h3><div class="row"><span>Einzelwickel</span><span>€ 32,00</span></div><div class="row"><span>10er Block, 10 + 1 gratis</span><span>€ 320,00</span></div></div>
    <div class="group"><h3>Hände</h3>
      <div class="row"><span>Klassische Maniküre mit Pflege oder Lack</span><span>€ 16,00</span></div>
      <div class="row"><span>Maniküre mit Handpeeling und Paraffinbad</span><span>€ 32,00</span></div>
      <div class="row"><span>Gel-Lack am Naturnagel</span><span>€ 16,00</span></div>
      <div class="row"><span>Nagelmodellage mit Gel, neues Set</span><span>€ 48,00</span></div>
      <div class="row"><span>Auffüllen inklusive Lack</span><span>€ 38,00</span></div>
      <div class="row"><span>Modellage entfernen mit Pflege</span><span>€ 16,00</span></div></div>
    <div class="photo portrait" role="img" aria-label="Porträtfoto einer geschminkten jungen Frau"></div>
  </div>
  <div class="panel">
    <div class="group"><h3>Permanente Wimpernverlängerung</h3>
      <div class="row"><span>erstes Set</span><span>€ 115,00</span></div>
      <div class="row"><span>Auffüllen innerhalb von 3 Wochen</span><span>€ 40,00</span></div>
      <div class="row"><span>Auffüllen innerhalb von 4-5 Wochen</span><span>€ 50,00</span></div></div>
    <div class="group"><h3>Enthaarung</h3>
      <div class="row"><span>Beine harzen inkl. Knie</span><span>€ 18,00</span></div>
      <div class="row"><span>Beine komplett harzen</span><span>€ 28,00</span></div>
      <div class="row"><span>Achseln harzen</span><span>€ 11,00</span></div>
      <div class="row"><span>Bikinizone harzen</span><span>€ 12,00</span></div>
      <div class="row"><span>Harzpackage klein</span><span>€ 38,00</span></div>
      <div class="row"><span>Männer: Rücken, Brust oder Bauch</span><span>€ 28,00</span></div></div>
    <div class="group"><h3>Make up</h3>
      <div class="row"><span>Dezentes Tagesmake up</span><span>€ 22,00</span></div>
      <div class="row"><span>Abendmake up</span><span>€ 28,00</span></div>
      <div class="row"><span>Hochzeitsmake up inkl. Probetermin</span><span>€ 48,00</span></div>
      <div class="row"><span>Brautpackage komplett</span><span>€ 199,00</span></div></div>
    <p class="note">Termine nach telefonischer Vereinbarung</p>
    <div class="photo orchid" role="img" aria-label="Foto einer pinken Orchidee mit Schminkpinseln"></div>
  </div>
</section>

<!-- Rückseite -->
<section class="sheet back">
  <div class="map" role="img" aria-label="Lageplan mit Straßen zum Studio"></div>
  <div class="brand"><span class="dot"></span>Glanzzeit</div>
  <div class="contact">
    <b>INHABERIN:</b><br>
    <span class="name">Marlene Vogt</span><br>
    Dipl. Kosmetikerin<br>Dipl. Make-up-Artist<br>Dipl. Nageldesignerin<br><br>
    Lindengasse 12<br>3100 Talheim<br>Telefon: 0660 1234567<br>E-Mail: glanzzeit@postfach.at<br><br>
    <b>ÖFFNUNGSZEITEN:</b><br>Termine nach telefonischer Vereinbarung
  </div>
  <div class="appointment">Ihr nächster Termin</div>
  <div class="bar" style="bottom:0;height:6px"></div>
</section>

</body>
</html>
```